Shopping center investment profile

We need to design a two-page 8.5" x 11" brochure that can be used as a template for profiling our shopping centers and demonstrating our track record to investors.

Our company (KVM Real Estate Investments) owns retail shopping centers in the southwestern United States. Our website is www.kvmtrh.example, but we will be redesigning and modernizing the website and logo in the near future, so please do not use the color schemes or framework of the website for the brochure.

Our investors are institutional and high net worth investors who typically have an existing relationship with our company. They are determining whether to invest multi-millions of dollars in a shopping center opportunity, so the brochure needs to be professional, very high quality and provide key information about the specific property.
Updates

Additional guidance on color scheme:

We would like to see a Blue (something like Hex #5A61BC) and Gold (Hex #EDB215) or (Hex #DDA24B) color scheme with some Black accents 

Thank you!

Target Market(s)

Our target audiences are institutional investors, high net-worth individuals, financial firms and medium to large commercial real estate companies.

Industry/Entity Type

Investment

Requirements
Must have
• Clean and modern look with corresponding fonts and colors.
• Incorporates the information found in the attached "Marlowe Crossing profile" Pages or PDF file.
• Final file design files that can be modified easily
Nice to have
• Two examples of industry brochures are attached. These are examples of the professional quality that we are looking for, not necessarily the design or format.

```html
<!DOCTYPE html>
<html lang="en">
<head>
<meta charset="utf-8">
<title>Marlowe Crossing – Property Profile</title>
<link rel="stylesheet" href="https://fonts.googleapis.com/css2?family=Montserrat:wght@300;400;600;700&family=Open+Sans:wght@400;600&display=swap">
<style>
:root{
  --blue:#565b8e;
  --blue-text:#4f5590;
  --gold:#dca447;
  --black:#141414;
  --ink:#2a2a2a;
  --grey:#7a7a7a;
  --white:#ffffff;
  --stage-light:#bdbdbd;
  --stage-dark:#8f8f8f;
}
*{box-sizing:border-box;margin:0;padding:0}
html,body{width:1200px;height:795px;overflow:hidden}
body{
  position:relative;
  font-family:"Montserrat",sans-serif;
  background:radial-gradient(ellipse at 50% 40%,var(--stage-light) 0%,var(--stage-dark) 100%);
}
.page-labels{position:absolute;left:0;top:0;width:1200px;height:80px}
.page-labels .label{position:absolute;top:27px;font-size:22px;font-weight:700;color:#1c1c1c;letter-spacing:.3px}
.page-labels .label-back{left:467px}
.page-labels .label-front{left:612px}
.page-labels .divider{position:absolute;left:599px;top:20px;width:1.5px;height:56px;background:#1c1c1c}
.page-labels .rule{position:absolute;left:465px;top:59px;width:275px;height:1px;background:#1c1c1c}

.page{
  position:absolute;top:75px;width:524px;height:677px;background:var(--white);
  overflow:hidden;box-shadow:0 4px 14px rgba(0,0,0,.35);
}
.page-back{left:68px}
.page-front{left:610px}

.title-block{position:absolute;left:24px;top:8px;width:196px;height:84px}
.title-block svg{position:absolute;inset:0}
.title-block .name{position:absolute;color:var(--white);font-weight:700;font-size:23px;line-height:1;white-space:nowrap}
.title-block .name-1{left:18px;top:12px}
.title-block .name-2{right:14px;top:44px}
.profile-title{position:absolute;left:230px;top:13px;font-size:25px;font-weight:300;color:var(--blue-text);letter-spacing:.3px}
.profile-bar{position:absolute;left:230px;top:48px;width:213px;height:17px;background:var(--gold)}
.profile-address{position:absolute;left:234px;top:76px;font-size:9px;line-height:11px;color:var(--grey);text-transform:uppercase;letter-spacing:.3px}

/* back page */
.tenants{position:absolute;left:15px;top:130px;width:130px}
.tenant{position:absolute;left:0;display:flex;align-items:center;gap:6px;font-size:13px;font-weight:600;color:var(--blue-text);white-space:nowrap}
.tenant .dot{width:14px;height:14px;border-radius:50%;background:var(--gold)}
.tenant-1{top:16px}
.tenant-2{top:108px}
.tenant-3{top:232px}

.photo{position:absolute}
.photo-before{left:192px;top:132px;width:150px;height:123px;background:linear-gradient(180deg,#c9d6e4 0%,#dfe3e6 45%,#9d8f7c 60%,#7f7b74 100%)}
.photo-after{left:345px;top:132px;width:149px;height:123px;background:linear-gradient(180deg,#3f5f91 0%,#7d9bc4 40%,#b9825b 58%,#8a5a40 80%,#9a9a98 100%)}
.ba-tag{position:absolute;top:147px;height:12px;padding:0 4px;background:var(--blue);color:var(--white);font-size:9.5px;font-weight:600;line-height:12px}
.ba-before{left:292px}
.ba-after{left:344px}
.site-plan{position:absolute;left:192px;top:260px;width:302px;height:162px;background:linear-gradient(135deg,#d7dfcd 0%,#b9c9a8 50%,#c9cfc4 100%)}

.challenges-title{position:absolute;left:16px;top:450px;font-size:22px;font-weight:700;line-height:28px;color:var(--blue-text);letter-spacing:.5px}
.challenges{position:absolute;left:204px;top:445px;width:303px;font-size:8.4px;line-height:10.6px;color:var(--grey)}
.challenges p{margin-bottom:2px}
.challenges strong{font-weight:700;color:var(--blue-text);font-size:9.5px;text-transform:uppercase}

.footer-band{position:absolute;left:0;top:635px;width:524px;height:42px;background:var(--gold);color:var(--white);font-size:9px}
.footer-band .address{position:absolute;left:22px;top:8px}
.footer-band .contact{position:absolute;left:383px;top:8px;line-height:12px}

/* front page */
.hero{position:absolute;left:0;top:115px;width:524px;height:520px;background:linear-gradient(180deg,#9aa6b4 0%,#c4c7c8 18%,#b88a63 35%,#a3704f 48%,#6e3b2a 60%,#c7c2ba 75%,#b6b3ad 100%)}
.front-shapes{position:absolute;left:0;top:0;width:524px;height:677px}
.summary{position:absolute;left:15px;top:380px;width:260px;color:var(--white)}
.summary h2,.investment h2{font-size:16.5px;font-weight:300;letter-spacing:.8px;margin-bottom:4px;white-space:nowrap}
.data-row{display:flex;font-size:10px;font-weight:300;line-height:12px;white-space:nowrap}
.data-row .key{width:120px}
.data-row .sep{width:13px}
.data-row .val strong{font-weight:600}
.data-row .full{width:auto}
.summary-rule{position:absolute;left:15px;top:505px;width:220px;height:1px;background:#bdbdbd}
.investment{position:absolute;left:15px;top:523px;width:260px;color:var(--white)}
.investment .key{width:130px}

.pitch{position:absolute;left:292px;width:230px;color:var(--ink)}
.pitch h2{font-size:19px;font-weight:700;letter-spacing:.8px;text-align:right;padding-right:3px;line-height:22px}
.pitch ul{list-style:none;font-family:"Open Sans",sans-serif;font-size:9px;line-height:11.8px;text-align:justify}
.pitch li::before{content:"• "}
.opportunity{top:291px}
.results{top:484px}

.tagline{position:absolute;left:14px;top:640px;color:var(--white);font-size:12px;font-weight:600;line-height:16px;letter-spacing:.4px}
.tagline .line-2{padding-left:50px}
.brand-badge{position:absolute;left:212px;top:612px;width:62px;height:50px;border-radius:50%;background:var(--white);display:flex;align-items:center;justify-content:center;text-align:center;font-size:7px;line-height:8px;font-weight:600;color:var(--blue-text)}
.front-contact{position:absolute;left:294px;top:642px;font-size:8.6px;line-height:11px;color:var(--ink)}
.front-contact .phone-web{position:absolute;left:107px;top:0;width:130px;padding-left:6px;border-left:1px solid var(--ink)}
</style>
</head>
<body>

<div class="page-labels">
  <span class="label label-back">Back Page</span>
  <span class="divider"></span>
  <span class="label label-front">Front Page</span>
  <span class="rule"></span>
</div>

<!-- back page -->
<section class="page page-back">
  <div class="title-block">
    <svg viewBox="0 0 196 84" width="196" height="84" aria-hidden="true"><polygon points="0,0 196,0 196,84 0,62" fill="var(--blue)"/></svg>
    <span class="name name-1">Marlowe</span>
    <span class="name name-2">Crossing</span>
  </div>
  <div class="profile-title">Property Profile</div>
  <div class="profile-bar"></div>
  <div class="profile-address">SWC of Alder Rd and Harlan Rd<br>Westfield, Arizona</div>

  <div class="tenants">
    <div class="tenant tenant-1"><span class="dot"></span>Citrine Table</div>
    <div class="tenant tenant-2"><span class="dot"></span>Cactus Cantina</div>
    <div class="tenant tenant-3"><span class="dot"></span>Starlight Lanes</div>
  </div>

  <div class="photo photo-before" role="img" aria-label="Shopping center storefronts before renovation"></div>
  <div class="photo photo-after" role="img" aria-label="Repainted shopping center storefronts after renovation"></div>
  <span class="ba-tag ba-before">Before</span>
  <span class="ba-tag ba-after">After</span>
  <div class="site-plan" role="img" aria-label="Site plan of the shopping center with parking and tenant pads"></div>

  <h2 class="challenges-title">CHALLENGES<br>AND<br>SOLUTIONS</h2>
  <div class="challenges">
    <p><strong>Nationwide vacancy rate</strong> – KVM did significant due diligence on the property before purchasing the asset, and determined that the location is an A/A–; Tenant improvement and leasing commissions were reserved in order to attract national and regional tenants</p>
    <p><strong>Size of anchor space</strong> – KVM determined that a family-friendly entertainment venue would best serve the demographics in the area instead of another grocer; KVM sought out an experienced operator in Starlight Lanes, who has multiple locations in three states</p>
    <p><strong>Curb appeal</strong> – With vacancy and a stigma attached to the center, KVM had to change the center's appeal to the community. KVM worked hand in hand with the Town of Westfield and the Copper Ridge Lakes community association to paint the center, upgrade landscaping and add new and larger monument signs</p>
  </div>

  <div class="footer-band">
    <span class="address">740 North Calloway | Suite 210 | Dunmore, Arizona 85999</span>
    <span class="contact">Phone &nbsp;: 555-014-2900<br>Web &nbsp;&nbsp;&nbsp;&nbsp;: www.kvmtrh.example</span>
  </div>
</section>

<!-- front page -->
<section class="page page-front">
  <div class="hero" role="img" aria-label="Rendering of the renovated shopping center with arched storefronts under a cloudy sky"></div>
  <svg class="front-shapes" viewBox="0 0 524 677" width="524" height="677" aria-hidden="true">
    <polygon points="0,255 275,395 275,635 0,635" fill="var(--black)"/>
    <path d="M270,635 L270,420 Q270,268 420,262 L524,258 L524,677 L0,677 L0,635 Z" fill="var(--gold)"/>
  </svg>

  <div class="title-block">
    <svg viewBox="0 0 196 84" width="196" height="84" aria-hidden="true"><polygon points="0,0 196,0 196,84 0,62" fill="var(--blue)"/></svg>
    <span class="name name-1">Marlowe</span>
    <span class="name name-2">Crossing</span>
  </div>
  <div class="profile-title">Property Profile</div>
  <div class="profile-bar"></div>
  <div class="profile-address">SWC of Alder Rd and Harlan Rd<br>Westfield, Arizona</div>

  <div class="summary">
    <h2>SUMMARY</h2>
    <div class="data-row"><span class="key">Property Type</span><span class="sep">:</span><span class="val"><strong>Shopping Center</strong></span></div>
    <div class="data-row"><span class="key">Size</span><span class="sep">:</span><span class="val">79,490 sq ft</span></div>
    <div class="data-row"><span class="key">Purchased</span><span class="sep">:</span><span class="val">April 2011</span></div>
    <div class="data-row"><span class="key">Total Investment</span><span class="sep">:</span><span class="val">$X,XXX,XXX</span></div>
    <div class="data-row"><span class="key">Purchase Occupancy</span><span class="sep">:</span><span class="val">8.39%</span></div>
    <div class="data-row"><span class="key">Current Occupancy</span><span class="sep">:</span><span class="val">97.29%</span></div>
    <div class="data-row"><span class="full">Projected 5-year IRR (Unleveraged) XX.XX%</span></div>
  </div>
  <div class="summary-rule"></div>
  <div class="investment">
    <h2>INVESTMENT INFORMATION</h2>
    <div class="data-row"><span class="key">Purchase Price</span><span class="val">$X,XXX,XXX</span></div>
    <div class="data-row"><span class="key">Sponsor Acquisition Fee</span><span class="val">$XX,XXX</span></div>
    <div class="data-row"><span class="key">Painting and Landscape</span><span class="val">$XXX,XXX</span></div>
    <div class="data-row"><span class="key">TI/LC Reserve</span><span class="val">$X,XXX,XXX</span></div>
    <div class="data-row"><span class="key">Operating Expenses</span><span class="val">$XXX,XXX</span></div>
  </div>

  <div class="pitch opportunity">
    <h2>OPPORTUNITY</h2>
    <ul>
      <li>Bank owned property with attractive purchase price</li>
      <li>Strong relationship with seller's broker and decision makers</li>
      <li>Redevelopment upside with management and leasing</li>
      <li>No major renovations required</li>
      <li>Westfield location has very strong population, education and income demographics</li>
      <li>Adjacent to premier 2,500-residence master planned community of Copper Ridge Lakes</li>
      <li>Strong employment area with the new Mesa Verde Regional hospital and the adjacent Halvorsen Cancer center</li>
    </ul>
  </div>
  <div class="pitch results">
    <h2>RESULTS</h2>
    <ul>
      <li>Stabilized the shopping center within three years, producing excellent results for investors</li>
      <li>Transformed the center into a vibrant destination that the surrounding community is excited about</li>
      <li>Transitioned legacy tenants to upgrade the business operators</li>
      <li>Reduced the shopping center's operating expenses by replacing vendors and appealing property taxes</li>
    </ul>
  </div>

  <div class="tagline"><div>making communities better</div><div class="line-2">one property at a time</div></div>
  <div class="brand-badge">KVM Real Estate Investments</div>
  <div class="front-contact">
    740 North Calloway<br>Suite 210<br>Dunmore, Arizona 85999
    <div class="phone-web">Phone &nbsp;: 555-014-2900<br>Web &nbsp;&nbsp;&nbsp;: www.kvmtrh.example</div>
  </div>
</section>

</body>
</html>
```